MRC New Busines Card

we need a business card for or renovation company, our main color is orange and our logo is a concrete ball rolling with MRC on it.the company name is Maple Ridge Contractors, Inc, we need somthing simple but profecional, also that we can change if its for roofing or renovations and the names

Target Market(s)

home owners

Industry/Entity Type

Concrete

Contact Information for Business Card

.

Colors
f68d4d
f9ba93
f37122
f78f20
faa54b
fbc994

```html
<!DOCTYPE html>
<html lang="en">
<head>
<meta charset="utf-8">
<title>Maple Ridge Contractors – Business Card</title>
<link href="https://fonts.googleapis.com/css2?family=Montserrat:wght@400;500;600;700;800&display=swap" rel="stylesheet">
<style>
  :root {
    --orange: #f78f20;
    --orange-deep: #f37122;
    --orange-light: #faa54b;
    --peach: #fbc994;
    --ink: #111111;
    --paper: #ffffff;
    --stone: #b5aa9c;
    --backdrop: #8a8a8a;
  }
  * { margin: 0; padding: 0; box-sizing: border-box; }
  html, body { width: 1200px; height: 900px; overflow: hidden; }
  body {
    background: var(--backdrop);
    font-family: "Montserrat", sans-serif;
    position: relative;
  }
  .card {
    position: absolute;
    left: 150px; top: 190px;
    width: 900px; height: 520px;
    border-radius: 34px;
    overflow: hidden;
    background: var(--paper);
  }
  .card-art { position: absolute; inset: 0; }
  .rep-name {
    position: absolute; left: 50px; top: 38px;
    font-size: 34px; font-weight: 700; color: var(--ink);
  }
  .rep-title {
    position: absolute; left: 52px; top: 84px;
    font-size: 21px; font-weight: 500; color: var(--paper);
  }
  .contact-list {
    position: absolute; left: 48px; top: 228px;
    list-style: none; color: var(--paper);
    font-size: 18px; font-weight: 500; line-height: 29px;
  }
  .contact-list li { display: flex; align-items: center; gap: 8px; white-space: nowrap; }
  .contact-list svg { width: 20px; height: 20px; flex: none; }
  .contact-list .indent { padding-left: 28px; }
  .credentials {
    position: absolute; left: 580px; top: 40px; width: 290px;
    text-align: center; font-size: 16px; font-weight: 500;
    letter-spacing: 3px; line-height: 26px; color: var(--ink);
  }
  .company-name {
    position: absolute; left: 530px; top: 300px; width: 350px;
    text-align: center; font-size: 30px; font-weight: 800;
    letter-spacing: 1px; line-height: 38px; color: var(--ink);
  }
  .service {
    position: absolute; top: 463px;
    font-size: 17px; font-weight: 600; line-height: 20px;
    letter-spacing: 6px; color: var(--orange-deep);
  }
  .service-roofing { left: 60px; }
  .service-painting { left: 290px; }
  .service-renovations { left: 610px; top: 452px; }
</style>
</head>
<body>
  <div class="card">
    <svg class="card-art" viewBox="0 0 900 520" width="900" height="520" aria-hidden="true">
      <defs>
        <linearGradient id="orangeField" x1="0" y1="0" x2="1" y2="1">
          <stop offset="0" stop-color="#f9a13a"/>
          <stop offset="1" stop-color="#f37122"/>
        </linearGradient>
        <clipPath id="orangeClip">
          <path d="M0 0 H420 C385 170 410 390 575 520 H0 Z"/>
        </clipPath>
      </defs>
      <path class="orange-field" d="M0 0 H420 C385 170 410 390 575 520 H0 Z" fill="url(#orangeField)"/>
      <path class="black-swoosh" d="M440 0 H570 C490 60 455 180 462 320 C440 210 425 90 440 0 Z" fill="var(--ink)"/>
      <rect class="service-band" x="30" y="456" width="600" height="34" fill="var(--peach)" opacity="0.7" clip-path="url(#orangeClip)"/>
      <line class="band-rule" x1="494" y1="440" x2="900" y2="440" stroke="var(--orange-deep)" stroke-width="2"/>
      <line class="band-rule" x1="536" y1="484" x2="900" y2="484" stroke="var(--orange-deep)" stroke-width="2"/>
      <circle class="mark-circle" cx="730" cy="180" r="78" fill="var(--stone)"/>
    </svg>

    <div class="rep-name">Dana Whitfield</div>
    <div class="rep-title">Sales Representative</div>

    <ul class="contact-list">
      <li><svg viewBox="0 0 24 24"><rect x="6" y="2" width="12" height="20" rx="2" fill="#111"/><rect x="8" y="5" width="8" height="7" fill="#fff"/></svg>770-555-0142</li>
      <li><svg viewBox="0 0 24 24"><path d="M5 3l4 1 1 5-2 2c1 3 3 5 6 6l2-2 5 1 1 4-3 2C10 22 2 14 3 6z" fill="#111"/></svg>404-555-0187</li>
      <li><svg viewBox="0 0 24 24"><rect x="7" y="2" width="10" height="7" fill="#111"/><rect x="3" y="9" width="18" height="9" rx="2" fill="#111"/><rect x="7" y="15" width="10" height="7" fill="#fff" stroke="#111"/></svg>770-555-0163</li>
      <li><svg viewBox="0 0 24 24"><rect x="2" y="5" width="20" height="14" fill="#111"/><path d="M2 5l10 8 10-8" fill="none" stroke="#fff" stroke-width="1.5"/></svg>Dana@MapleRidgeContractors.com</li>
      <li><svg viewBox="0 0 24 24"><circle cx="12" cy="12" r="10" fill="none" stroke="#111" stroke-width="2"/><path d="M2 12h20M12 2c-5 6-5 14 0 20M12 2c5 6 5 14 0 20" fill="none" stroke="#111" stroke-width="1.5"/></svg>www.MapleRidgeContractors.com</li>
      <li><svg viewBox="0 0 24 24"><path d="M12 2L1 12h3v10h6v-6h4v6h6V12h3z" fill="#111"/></svg>4120 Cedar Bend Ln</li>
      <li class="indent">Millbrook, GA 30099</li>
    </ul>

    <div class="credentials">FREE ESTIMATES<br>LICENSED &amp; INSURED</div>
    <div class="company-name">MAPLE RIDGE<br>CONTRACTORS</div>

    <div class="service service-roofing">ROOFING</div>
    <div class="service service-painting">PAINTING</div>
    <div class="service service-renovations">RENOVATIONS</div>
  </div>
</body>
</html>
```